Briney Lark Fare landing page design

We need a landing page designed for an ecommerce website that sales fresh US domestic shrimp from the Gulf of Mexico and ships them direct to the consumer "From Our Shore To Your Door". For the landing page, we would like customers to be able to place an order and or inquire further about our product as well as links to social media. The company logo is attached

1 page

```html
<!DOCTYPE html>
<html lang="en">
<head>
<meta charset="utf-8">
<title>Briney Lark Fare — From our shore to your door</title>
<link rel="stylesheet" href="https://fonts.googleapis.com/css2?family=Montserrat:wght@400;500;600;700&display=swap">
<style>
:root{
  --orange:#ee884a;
  --orange-dark:#d0703a;
  --blue:#35a8e2;
  --line-blue:#6cc0ec;
  --ink:#555a5e;
  --ink-soft:#6a6f73;
  --white:#ffffff;
  --star:#79c56a;
}
*{box-sizing:border-box;margin:0;padding:0}
html,body{width:717px;height:1200px;overflow:hidden;background:var(--white)}
body{font-family:'Montserrat',sans-serif;color:var(--ink);position:relative}
.abs{position:absolute}
a{color:inherit;text-decoration:none}

.site-header{position:absolute;left:0;top:0;width:717px;height:31px;background:var(--white)}
.brand{left:94px;top:6px;display:flex;align-items:center;gap:5px;font-size:9px;font-weight:600;color:var(--ink);letter-spacing:.5px}
.brand-dot{width:19px;height:19px;border-radius:50%;border:1px solid #c9cdd0}
.main-nav{left:275px;top:11px;display:flex;gap:16px;font-size:7.6px}
.main-nav .active{color:var(--orange)}
.btn{display:flex;align-items:center;justify-content:center;background:var(--orange);color:var(--white);border-radius:2px;font-size:7.4px;letter-spacing:.4px}
.btn-shop{left:570px;top:9px;width:53px;height:15px;font-size:6.4px}

.hero{left:0;top:31px;width:717px;height:269px;background:linear-gradient(160deg,#1f6f78 0%,#2f8f94 35%,#5fb2ad 55%,#cfd9d4 72%,#ecebe6 100%)}
.hero-title{left:0;top:120px;width:717px;text-align:center;color:var(--white);font-size:25px;font-weight:700}
.hero-sub{left:0;top:150px;width:717px;text-align:center;color:var(--white);font-size:11.5px;letter-spacing:.3px}
.btn-hero{left:314px;top:184px;width:89px;height:22px}

.section-title{left:0;width:717px;text-align:center;font-size:13.5px;font-weight:600;letter-spacing:.5px;color:var(--ink)}
.section-title span{display:inline-block;padding:0 3px 3px;border-bottom:1px solid var(--line-blue)}
.steps-title{top:318px}
.step-ring{width:73px;height:73px;border-radius:50%;border:1.6px solid var(--line-blue);display:flex;align-items:center;justify-content:center}
.step-name{font-size:13.5px;color:var(--orange);letter-spacing:.3px}
.step-copy{font-size:7.6px;line-height:9px;color:var(--ink-soft);margin-top:3px;letter-spacing:.2px}
.step-right{left:440px}
.step-left{right:440px;text-align:right}
.btn-learn{left:314px;top:614px;width:89px;height:21px}

.salad-photo{left:0;top:658px;width:358px;height:242px;background:radial-gradient(circle at 45% 55%,#f0a070 0%,#e08458 20%,#7c8a4a 45%,#4e5a30 65%,#c7b7a8 85%,#eee 100%)}
.love-panel{left:358px;top:658px;width:359px;height:242px;background:var(--blue);color:var(--white);padding:24px 12px 0 13px}
.love-panel h2{font-size:13.6px;font-weight:600;letter-spacing:.4px;margin-bottom:17px}
.love-panel p{font-size:7.7px;line-height:10.8px;margin-bottom:10.6px;letter-spacing:.1px}

.reviews-title{top:918px}
.review{width:120px;text-align:center}
.stars{display:flex;justify-content:center;gap:2px;height:13px}
.review p{font-size:7.6px;line-height:8.6px;color:var(--ink-soft);margin-top:4px}
.review-name{font-size:7.6px;font-weight:600;margin-top:4px;color:var(--ink)}
.carousel-arrow{font-size:15px;color:#9a9ea1;top:979px}
.more-reviews{left:0;top:1036px;width:717px;text-align:center;font-size:7.6px;color:var(--ink)}
.more-reviews b{color:var(--star);font-size:6px}

.site-footer{left:0;top:1066px;width:717px;height:112px;background:var(--orange);color:var(--white)}
.footer-links{left:130px;top:20px;font-size:7.6px;line-height:14.4px;list-style:none}
.footer-heading{font-size:8.4px;font-weight:600;padding:0 3px 2px;border-bottom:1px solid var(--white)}
.social-heading{left:303px;top:12px}
.social{top:38px;width:27px;height:27px;border-radius:50%;background:var(--white)}
.contact-heading{left:521px;top:12px}
.contact-copy{left:524px;top:36px;width:66px;font-size:7.6px;line-height:8.6px}
.legal-bar{left:0;top:1178px;width:717px;height:22px;background:var(--orange-dark);color:var(--white);font-size:6.4px}
.legal-bar .copy{left:94px;top:7px}
.legal-bar .links{left:572px;top:5px;display:flex;gap:8px}
</style>
</head>
<body>
<header class="site-header">
  <div class="abs brand"><span class="brand-dot"></span>BRINEY LARK FARE</div>
  <nav class="abs main-nav"><a class="active">Home</a><a>How It Works</a><a>Menu</a><a>About</a></nav>
  <a class="abs btn btn-shop">SHOP NOW</a>
</header>

<section class="abs hero" role="img" aria-label="Aerial photo of a turquoise gulf shoreline meeting white sand"></section>
<h1 class="abs hero-title">From our shore to your door</h1>
<p class="abs hero-sub">Fresh Shrimp delivered directly at your doorstep.</p>
<a class="abs btn btn-hero">GET STARTED</a>

<h2 class="abs section-title steps-title"><span>HOW IT WORKS</span></h2>

<div class="abs step-ring" style="left:358px;top:354px">
  <svg width="38" height="30" viewBox="0 0 38 30" fill="none" stroke="#6cc0ec" stroke-width="1.3"><rect x="6" y="3" width="26" height="18" rx="1.5"/><path d="M2 23h34l-2 3H4z"/><path d="M13 8h2l2 7h7l2-5H16"/><circle cx="18" cy="17.5" r="1"/><circle cx="23" cy="17.5" r="1"/></svg>
</div>
<div class="abs step-right" style="top:370px"><div class="step-name">Choose the order</div><div class="step-copy">Lorem ipsum dolor sit amet,<br>consectetur adipiscing elit.</div></div>

<div class="abs step-ring" style="left:286px;top:436px">
  <svg width="42" height="30" viewBox="0 0 42 30" fill="none" stroke="#6cc0ec" stroke-width="1.3"><rect x="2" y="4" width="24" height="18"/><path d="M26 10h8l5 6v6H26"/><circle cx="10" cy="24" r="3"/><circle cx="32" cy="24" r="3"/><circle cx="14" cy="13" r="4.5"/></svg>
</div>
<div class="abs step-left" style="top:452px"><div class="step-name">We deliver</div><div class="step-copy">Lorem ipsum dolor sit amet,<br>consectetur adipiscing elit.</div></div>

<div class="abs step-ring" style="left:358px;top:518px">
  <svg width="36" height="30" viewBox="0 0 36 30" fill="none" stroke="#6cc0ec" stroke-width="1.3"><circle cx="20" cy="4" r="1.8"/><path d="M8 17a12 11 0 0 1 24 0z"/><path d="M6 17h28"/><path d="M2 22l6-3h8l4 2h-7"/><path d="M2 27l5-2h10l10-6"/></svg>
</div>
<div class="abs step-right" style="top:534px"><div class="step-name">You enjoy</div><div class="step-copy">Lorem ipsum dolor sit amet,<br>consectetur adipiscing elit.</div></div>

<a class="abs btn btn-learn">LEARN MORE</a>

<div class="abs salad-photo" role="img" aria-label="Close-up photo of a salad with grilled shrimp, greens and radish"></div>
<section class="abs love-panel">
  <h2>WHY YOU WILL LOVE OUR SHRIMPS</h2>
  <p>Lorem ipsum dolor sit amet, consectetur adipiscing elit. Suspendisse mollis sit amet ligula vit ae commodo.</p>
  <p>Pellentesque habitant morbi tristique senectus et netus et malesuada fames ac turpis egestas. Ut viverra consequat venenatis. Vestibulum scelerisque, lacus a pulvinar condimentum, nisi orci luctus dui, at molestie libero quam sit amet enim. Vivamus dictum venenatis tincidunt.</p>
  <p>Morbi viverra arcu ac quam pharetra egestas. Sed consequat lacus sed mauris fermentum ultricies. Pellentesque id neque magna. Ut et mi sed sem maximus rhoncus id eu arcu. Vestibulum volutpat elit sapien, ut cursus massa congue laoreet.</p>
  <p>Pellentesque habitant morbi tristique senectus et netus et malesuada fames ac turpis egestas.</p>
</section>

<h2 class="abs section-title reviews-title"><span>WHAT OUR CUSTOMERS ARE SAYING</span></h2>
<span class="abs carousel-arrow" style="left:98px">&lt;</span>
<span class="abs carousel-arrow" style="left:607px">&gt;</span>

<svg width="0" height="0" style="position:absolute"><defs><polygon id="star" points="6.5,0 8.3,4.4 13,4.7 9.4,7.8 10.5,12.4 6.5,9.9 2.5,12.4 3.6,7.8 0,4.7 4.7,4.4" fill="#79c56a"/></defs></svg>

<div class="abs review" style="left:124px;top:953px">
  <div class="stars"><svg width="13" height="13"><use href="#star"/></svg><svg width="13" height="13"><use href="#star"/></svg><svg width="13" height="13"><use href="#star"/></svg><svg width="13" height="13"><use href="#star"/></svg><svg width="13" height="13"><use href="#star"/></svg></div>
  <p>Lorem ipsum dolor sit amet, consectetur adipiscing elit, sed do eiusmod tempor incididunt ut labore et</p>
  <div class="review-name">Dave S</div>
</div>
<div class="abs review" style="left:298px;top:953px">
  <div class="stars"><svg width="13" height="13"><use href="#star"/></svg><svg width="13" height="13"><use href="#star"/></svg><svg width="13" height="13"><use href="#star"/></svg><svg width="13" height="13"><use href="#star"/></svg><svg width="13" height="13"><use href="#star"/></svg></div>
  <p>Lorem ipsum dolor sit amet, consectetur adipiscing elit, sed do eiusmod tempor incididunt ut labore et</p>
  <div class="review-name">Christina</div>
</div>
<div class="abs review" style="left:471px;top:953px">
  <div class="stars"><svg width="13" height="13"><use href="#star"/></svg><svg width="13" height="13"><use href="#star"/></svg><svg width="13" height="13"><use href="#star"/></svg><svg width="13" height="13"><use href="#star"/></svg><svg width="13" height="13"><use href="#star"/></svg></div>
  <p>Lorem ipsum dolor sit amet, consectetur adipiscing elit, sed do eiusmod tempor incididunt ut labore et</p>
  <div class="review-name">Karen</div>
</div>
<a class="abs more-reviews">See more reviews <b>&#9654;</b></a>

<footer class="abs site-footer">
  <ul class="abs footer-links"><li>Home</li><li>How it works</li><li>Menu</li><li>About</li></ul>
  <div class="abs footer-heading social-heading">Follow our Social Media</div>
  <a class="abs social" style="left:301px" aria-label="Social link"></a>
  <a class="abs social" style="left:345px" aria-label="Social link"></a>
  <a class="abs social" style="left:389px" aria-label="Social link"></a>
  <div class="abs footer-heading contact-heading">Contact</div>
  <p class="abs contact-copy">Lorem ipsum dolor sit amet, consectetur adipiscing elit,</p>
</footer>
<div class="abs legal-bar">
  <span class="abs copy">© 2019 Briney Lark Fare.</span>
  <span class="abs links"><a>Privacy</a><a>Terms</a></span>
</div>
</body>
</html>
```